My Professional Resume/CV Design

Hi Pixel Harbor experts, I need a professional resume/CV design for using my carrier hiring activities. I have a draft and this draft is 2 types.
1) Traditional IT Major Company Senior(Manager Level) to Director level application (File: Tanabe_Emiko_Res_EN2023AprA)
>Application example companies: Velmora, Drakt, Quindle, Brightmarsh, HoltenWare, Fenwick Ridge, Zentravix, Morivon, Quorexa, Plinth, dZop, Kelvarna etc
>This should not be fancy. Please make format with traditional/gentle/standard but also need to appear unique point such as icons, borderlines etc
2) Cutting-Edge (Web 3.0/metaverse/NFT/Crypto) Start-up or Young (Less 5 year's history) Company Director and C-Levels position application (Tanabe_Emiko_Res_EN2023Apr_typeC)
>Application Example Companies: Tessaluk Studios, Vorlexa, Zintaro.example, Wovenpath, Lumbrook, FernPocket, Thaxel, Kipa/Dult/Snov, Morvik, QUESTAN, wordLYM etc
>This resume format should be something "edge" "advanced" "future" and "high-tech", so need to your high sense of design technics.
Both drafts is without a profile picture, but I need to put in my portfolio picture (Just attached one is my 2018's, you can trim and edit as well)
For the document format, please send me to WORD and PAGES both. and total MAX 2 page in all contents please (No more 3 pages)
Target Market(s)
Traditional Major Tech Company's VP/Directors or/and Latest Web 3.0 StartUp C-Levels (CEO/CTO/CSO/COO etc)
Industry/Entity Type
Technology
Font styles to use
Other font styles liked:
- Choose 3 a)Century Gothic b) Avenir c)Graphik d)Kohinoor e)Optima f)Platino
Look and feel
Each slider illustrates characteristics of the customer's brand and the style your logo design should communicate.

```html
<!DOCTYPE html>
<html lang="en">
<head>
<meta charset="utf-8">
<title>Emiko Tanabe – Resume</title>
<link rel="stylesheet" href="https://fonts.googleapis.com/css2?family=Lato:wght@400;700;900&display=swap">
<style>
:root{
  --stage:#f1f1f1;
  --paper:#ffffff;
  --brand:#2c5d8f;
  --band:#e2e2e2;
  --ink:#1d1d1d;
  --muted:#555555;
  --photo-a:#c9b8ad;
  --photo-b:#7d8fa6;
}
*{margin:0;padding:0;box-sizing:border-box}
html,body{width:1200px;height:859px;overflow:hidden;background:var(--stage)}
body{position:relative;font-family:"Lato",Arial,sans-serif;color:var(--ink)}
.page{position:absolute;top:66px;width:518px;height:730px;background:var(--paper);box-shadow:0 1px 6px rgba(0,0,0,.18);overflow:hidden;padding:0 14px 0 16px;font-size:6.85px;line-height:8.3px}
.page-one{left:70px}
.page-two{left:614px;padding-top:8px}
.masthead{position:relative;height:128px;margin:0 -14px 0 -16px}
.masthead-band{position:absolute;left:0;right:0;top:43px;height:46px;background:var(--brand)}
.portrait{position:absolute;left:20px;top:8px;width:74px;height:118px;background:linear-gradient(160deg,var(--photo-a),var(--photo-b))}
.name{position:absolute;left:140px;top:49px;font-family:"Lato",sans-serif;color:#fff;font-size:24px;line-height:24px;letter-spacing:.4px;font-weight:900}
.location{position:absolute;left:142px;top:75px;color:#fff;font-size:10px;line-height:11px}
.contact{position:absolute;left:150px;top:101px;color:var(--muted);font-size:7px;line-height:9px}
.contact svg{vertical-align:-1px;margin-right:4px}
.headline{background:var(--band);margin:0 -14px 0 -16px;text-align:center;font-weight:700;font-size:6.9px;line-height:8.4px;padding:1px 0}
.summary{margin-top:4px;text-align:justify}
.section-title{background:var(--band);margin:6px -14px 5px -16px;text-align:center;font-weight:700;font-size:7px;line-height:11px}
ul.points{padding-left:16px}
ul.points li{margin-bottom:.5px}
.competencies{display:grid;grid-template-columns:1.05fr 1fr 1fr;padding:0 6px 0 20px;list-style:none}
.competencies li{position:relative;padding-left:10px}
.competencies li::before{content:"";position:absolute;left:0;top:2.8px;width:3px;height:3px;border-radius:50%;background:var(--ink)}
.job{margin-bottom:5px}
.job-head{display:flex;justify-content:space-between;font-weight:700}
.job p{text-align:justify}
.running-head{background:var(--band);margin:4px -14px 6px -16px;text-align:center;font-weight:700;font-size:6.9px;line-height:11px}
</style>
</head>
<body>

<section class="page page-one">
  <header class="masthead">
    <div class="masthead-band"></div>
    <div class="portrait" role="img" aria-label="Portrait photo of the candidate in a light suit"></div>
    <h1 class="name">EMIKO TANABE</h1>
    <div class="location">Wanchai, Hong Kong</div>
    <div class="contact">
      <div><svg width="7" height="5" viewBox="0 0 6 5"><rect x=".3" y=".3" width="5.4" height="4.4" fill="none" stroke="#555" stroke-width=".6"/><path d="M.3 .3 3 2.6 5.7 .3" fill="none" stroke="#555" stroke-width=".6"/></svg>etanabe512@mail.example</div>
      <div><svg width="7" height="7" viewBox="0 0 6 6"><path d="M1 .5h1.2l.6 1.4-.8.6a3.5 3.5 0 0 0 1.5 1.5l.6-.8 1.4.6v1.2C3 5 1 3 1 .5z" fill="#555"/></svg>+852 5100 2040 | 5100 7715</div>
    </div>
  </header>

  <div class="headline">BUSINESS DEVELOPMENT | VENDOR MANAGEMENT | PARTNER CHANNEL SALES<br>Web 3+ Technology &amp; Cyber Security / Strategic Planning &amp; Execution / Proposal &amp; Contract Management</div>

  <p class="summary">My value and career will only increase in a diverse and multinational work environment. High-impact growth-oriented professional demonstrating a strong grasp of current marketing tools and strategies aligned with cutting-edge technology with an interest in the transformation of society/era events within the industry and cyber security with an entrepreneurial spirit. Strategically collaborate with external vendors and internal business partners, manages various commercial platforms, systems, domains, and channels to ensure scale marketing and lead development capabilities in line with business growth plans that deliver high-quality results. Participate in supply chain strategy development, developing implementation plans, and methods of dealing with business. Display strong analytical ability to evaluate end-to-end customer experience across multiple channels and customer touchpoints. Highly creative with experience in identifying target audiences and devising digital campaigns while valuing traditional methods that engage, inform, and motivate while staying abreast of industry trends. Conclude below 3 is my core abilities.<br>"Cutting-Edge Technologies" "Business Development" and "Japan/APAC/Global Channel Sales"</p>

  <h2 class="section-title">HIGHLIGHTS OF QUALIFICATION</h2>
  <ul class="points">
    <li>Expert levels of sense of abilities in conducting marketing research and analyzing data strategically to identify brand/product value propositions, prospect customers, markets, and major competitors</li>
    <li>Understands target audiences and competition dynamics with insights from various sources while leading integrated digital and offline marketing campaigns from concept to execution, on time and within scope and budget.</li>
    <li>Serve as supply chain interface for all major projects, with clear knowledge of project progress, logistics, and distribution development as well as implementation and execution of local and regional projects.</li>
    <li>Fluent in English and Japanese to communicate compelling value propositions for existing / prospective customers through different channels, digital/social communication, partnership, and sponsorship regularly and on a project basis.</li>
    <li>Conceptualize and develop brand/product sales plans and campaigns for companies and individual business lines, including planning, liaison, coordination, and execution.</li>
  </ul>

  <h2 class="section-title">CORE COMPETENCIES</h2>
  <ul class="competencies">
    <li>Global Operations Management</li><li>Key Account Management</li><li>Staff Training / Retention</li>
    <li>Strategic Partnerships</li><li>Business Restructuring</li><li>Business Administration</li>
    <li>Process Improvement Champion</li><li>Team Leadership / Management</li><li>Supply Chain Management</li>
    <li>Strategic Planning &amp; Execution</li><li>P &amp; L / Revenue Growth</li><li>Vendor / Partner Management</li>
    <li>Cryptocurrency | B2B B2B2C</li><li>Budget Management</li><li>Negotiations &amp; Agreements</li>
    <li>Research &amp; Development</li><li>Channel Sales B2B + B2G</li><li>Records &amp; Documentation</li>
  </ul>

  <h2 class="section-title">PROFESSIONAL EXPERIENCE</h2>
  <article class="job">
    <div class="job-head"><span>Inside Renewals Sales | Corvane Networks. | Hong Kong |</span><span>Jul 2022 - Present</span></div>
    <p>First visa-sponsored employee since the establishment of the APAC Hong Kong company (2017 and in total over 100+). Promotion to Territory Manager (Inside New Sales) is factored in. The agreement to start with renewal sales was to be able to build relationships with existing partners and to set the stage for the new position. Due to internal circumstances, there is no budgetary visibility for an Inside Sales Manager for the Japan Territory. Job hunting activity while still employed for reasons of wanting to advance own careers external, as prospects for promotion within the company are very low expectations by company reasons.</p>
    <ul class="points">
      <li>Distributor and Reseller (Partner) Management: Before I join, Corvane was the low position for any of the partner's sales, like quotation production due to only focused PO. I focusing what end users face on the problems and pain and shared with proper partners. A result, they never ask me for a quotation (they now can quote themself) and they proposed me to new sales plans and strategies. I just concentrated to do what my partner want and relationship development.</li>
      <li>Co-work with Territory Regional Team remotely: Mainly Japan Sales, SEs, CS, Technical Support</li>
      <li>Enhancing mutual synergies with other regional teams: Corporate team works with especially APAC another region team ( India/ SEA/ANZ/China total 4 regions) and US and EMEA as well.</li>
    </ul>
  </article>
  <article class="job">
    <div class="job-head"><span>Guild Business Division Sales Operation Head | Hexlot Job Japan | Hong Kong | Part-Time</span><span>Early 2022</span></div>
    <p>This entity is an NFT GameFi startup for "Play To Earn" players scholarship program. I joined as the authorized person under CEO. My role is a huge territory, from community management to design strategy and tactics for this scholarship business.</p>
  </article>
  <article class="job">
    <div class="job-head"><span>Business Development Manager | ORT HK Limited | Hong Kong</span><span>Apr 2021 - Apr 2022</span></div>
    <p>Join from GM's direct invitation due to he wanna survive the pandemic crisis, this is an IT reseller business provider in Hong Kong.</p>
  </article>
</section>

<section class="page page-two">
  <p>China, SEA, and Japan market. Upon long-term mainly prospective business development and strategy, then proposed better to downsizing and restructuring, I suggest leaving this company and GM accepted (Still best relationships)</p>

  <div class="running-head">EMIKO TANABE | ETANABE512@MAIL.EXAMPLE | +852 5100 2040/5100 7715 | PAGE 2</div>

  <article class="job">
    <div class="job-head"><span>Business Development Manager | MIRA High-Tech (Hong Kong) Limited | Hong Kong</span><span>Aug 2020 – Apr 2021</span></div>
    <p>Start from BD of medical digital devices (Organic disinfection water, robotic UV lamps) constructing frameworks for saving COVID-19 pandemic. After the project timeline and to-dos were fixed, received direct offer from president of next company to move on.</p>
  </article>
  <article class="job">
    <div class="job-head"><span>Business Development Manager | Pell Global | Hong Kong</span><span>Apr2019 –Mar 2020</span></div>
    <p>Demonstrate mastery in the production of a new TV program with Gulfline National News (TV station) for introducing cutting-edge science such as human-type robots; creating program/production budgets and completed all interactions with the research institute on behalf of the TV station and also planned the 12 episodes of the first episode</p>
  </article>
  <article class="job">
    <div class="job-head"><span>Head of Division | Ovanthel Tech Limited(Former Qorvath Consulting, Company name changes) | Hong Kong</span><span>Sep 2018 – Mar 2019</span></div>
    <p>Pioneered a zero-based customized Crypto Exchange platform, overseeing process improvement initiatives and facilitating prompt delivery to clients. Direct staff operations for the total IEO / STO business production, building and maintaining strategic relationships with all levels of stakeholders. Earned 3million HK$ in 3 months of working on the BPO's contract for the establishment of cryptocurrency exchange and new products (token), delivering the product by the deadline and succeeded in restructuring a negative company business into a profit-oriented enterprise. Stellar record of outperforming corporate expectations in meeting goals and objectives while strengthening effective communications with internal stakeholders, vendor and client team members.</p>
    <ul class="points">
      <li>Participated in high-profile business trip meetings, managed and oversaw daily chat communications as well as prepared and presented operational reports to management and key stakeholders.</li>
      <li>Orchestrate the provision of outstanding oversight for five diverse internal departments and three regions (HK, Philippines and Japan) utilizing multiple business management software and remote work applications including video meetings.</li>
      <li>Exceeded expectations in creating and managing content for movies and documents including white paper writing, Community Management, increasing market positioning, and optimizing revenue growth.</li>
      <li>Appraised for developing and delivering tokens to clients using exceptional customer service management to generate business while facilitating customers' integration wallet and listing exchange for a casino operator's ICO project.</li>
      <li>Mastermind the process of instituting infrastructures and external vendor systems such as Customer Due Diligence, and trading systems to the ICO platform.</li>
      <li>Displayed solid leadership abilities in team building / mentoring activities and optimized project branding processes involving HR oversight and staffing as well as financial control for the ICO project.</li>
      <li>Recognized for extensive financial acumen and expertise in budget controls (P&amp;L, BS), generated a record $1.2 M in profit and achieved all ICO requirements while successfully listing one exchange at a time.</li>
      <li>Accomplished in diverse Ad-hoc operations encompassing accounting, payroll management, contract oversight, as well as corporate liaison with vendors, exchanges and other multi-functional professionals involved in project works</li>
    </ul>
    <p>*As I could not expect any further promotion, I transfer to further develop my career and gain multi-national business acumen.</p>
  </article>
  <article class="job">
    <div class="job-head"><span>Senior Manager | Qorvath Consulting International, Hong Kong</span><span>May 2016 - Sep 2018 (Mar 2019)</span></div>
    <p>Outperformed corporate expectations in leading and supervising cryptocurrency white label exchange operations by improving systems that cannot be managed by email / chats, utilizing project management software, solving unexpected issues, and implementing process improvement initiatives and manuals. Adept in managing multiple projects, achieving stable operational exchange, and contributing to end user increase from 1500 to 5000. Reputed for consistent updates to the ever-changing customers' desired requirements on the platform to achieve strategic goals. Named as Taiwan's market project leader by the CEO, overseeing a remote team of professionals located in Tokyo, Osaka, Hong Kong, and Europe. Monitored specific project progress and status while also communicating and liaising between client and Fintech Service Vendors (B2B and B2C businesses) to build consensus.</p>
    <ul class="points">
      <li>Played a key role in leading and managing Customer Due Diligence (KYC/KYB) operations including the creation manual to manage risk and prevent financial misconduct for CS (Customer Success)</li>
      <li>Competently developed new tokens and adhered to clients' requests in establishing an on-time implementation exchange platform to ease the process of exchanging major cryptocurrencies such as BTC/ETH/LTC</li>
      <li>Promptly delivered exchange debit cards linked with the customers' cryptocurrency wallet while crypto compliance changes</li>
      <li>Spearheaded global business operations while overseeing the Taiwan subsidiary business expansion set up to encompass crypto-to-fiat trading, hiring and training staff, deposit/withdrawal operations to Taiwanese partner b2b clients, and bulk trading. Generated 500 users before handover to the local manager.</li>
    </ul>
    <p>*Company name just changed from Qorvath Consulting International Limited to Ovanthel Tech Limited (Same Shareholders)</p>
  </article>
  <article class="job">
    <div class="job-head"><span>Project Manager | PT. SERIMA BALI | Denpasar</span><span>2014 – 2015</span></div>
    <p>Strategic planning of corporate projects with B2B institutions at Bali of Indonesia Microfinance and Property Corporate.<br>*Relocate to Hong Kong by personal reason at the time late 2015</p>
  </article>
  <article class="job">
    <div class="job-head"><span>Chief Operation Officer | Tropos Agency | Tokyo</span><span>2010 – 2014</span></div>
    <p>Structured and pioneered the process of running the Tokyo branch of a Singaporean restaurant by connecting with the F&amp;B company. Demonstrated strength in PR including the English Media to increase brand awareness and clientele growth.<br>*The business cessation requirements of the JV Agreement are met. (Reason cannot be given due to confidentiality, but I can answer orally)</p>
  </article>

  <h2 class="section-title">EDUCATION</h2>
  <p>Bachelor's degree in economics/Philosophy | University of Kanto, Japan</p>
</section>

</body>
</html>
```